"End of year wishes" - Electronic card

Quenlax is a regulatory consulting company in the cosmetic sector. We provide premium services and have 12 years of experience.
Please visit our website for more information: https://quenlax.example
Like every year, we would like to send an electronic design to our clients and partners to wish them happy holidays. This year, we would like to share two good news with them: offer them a surprise (to be revealed later on) and invite them to visit our new brand new website. We relay on your talent and imagination for the design! We need something very professional, serious, beautiful and in line with our graphic layout (see our company website)

Target Market(s)

cosmetic brands

Industry/Entity Type

Cosmetics

Requirements
Must have
• The following statement should be included to the design:

We wish you a Happy Holiday and a Marvelous New Year 2021!
As December is the month of giving, we have a surprise for you. Please contact your dedicated Account Manager to find out more!

Good news never comes alone, we've also updated our website in order to serve you better. We hope you like it as much as we do.
Please enjoy the experience: www.quenlax.example

```html
<!DOCTYPE html>
<html lang="en">
<head>
<meta charset="utf-8">
<title>Quenlax – Season's Greetings 2021</title>
<link rel="stylesheet" href="https://fonts.googleapis.com/css2?family=Courgette&family=Roboto:wght@400;700&family=Poppins:wght@800&display=swap">
<style>
  :root {
    --gold-light: #efe3ad;
    --gold-mid: #d9c27a;
    --gold-deep: #b9964e;
    --pine: #3f7d2c;
    --pine-dark: #1f5219;
    --teal: #0f8f70;
    --teal-dark: #07443b;
    --digit-edge: #e6c45c;
    --frame-wood: #b88d5e;
    --frame-edge: #8a6238;
    --card-paper: #ebdfa6;
    --script-red: #c4180e;
    --ink: #111111;
    --tag-paper: #c9a173;
  }
  * { box-sizing: border-box; margin: 0; padding: 0; }
  html, body { width: 844px; height: 1200px; overflow: hidden; background: var(--gold-mid); }
  .card {
    position: relative;
    width: 844px;
    height: 1200px;
    overflow: hidden;
    font-family: "Roboto", Arial, sans-serif;
    background: linear-gradient(150deg, var(--gold-light) 0%, var(--gold-mid) 55%, var(--gold-deep) 100%);
  }

  /* Pine and ornament zones */
  .pine-zone { position: absolute; }
  .pine-top-left {
    left: -120px; top: -120px; width: 520px; height: 460px;
    border-radius: 50%;
    background: radial-gradient(closest-side, var(--pine-dark) 0%, var(--pine) 55%, rgba(63,125,44,0) 100%);
  }
  .pine-top-right {
    left: 560px; top: -140px; width: 420px; height: 460px;
    border-radius: 50%;
    background: radial-gradient(closest-side, var(--pine-dark) 0%, var(--pine) 55%, rgba(63,125,44,0) 100%);
  }
  .pine-bottom {
    left: -60px; top: 1000px; width: 964px; height: 360px;
    border-radius: 50%;
    background: radial-gradient(closest-side, var(--pine-dark) 0%, var(--pine) 60%, rgba(63,125,44,0) 100%);
  }

  /* Year title */
  .year-title {
    position: absolute;
    inset: 0;
    font-family: "Poppins", Arial, sans-serif;
    font-weight: 800;
    font-size: 200px;
    line-height: 1;
    pointer-events: none;
  }
  .year-digits {
    position: absolute;
    top: 92px;
    color: var(--teal);
    -webkit-text-stroke: 3px var(--digit-edge);
    text-shadow: 7px 6px 0 var(--teal-dark);
    letter-spacing: -8px;
    transform: scaleY(1.3);
    transform-origin: 50% 170px;
  }
  .year-digits-lead { left: 172px; }
  .year-digits-tail { left: 478px; }
  .year-ornament {
    position: absolute;
    left: 305px; top: 68px;
    width: 178px; height: 212px;
    border-radius: 22px;
    background: linear-gradient(180deg, var(--teal) 0%, var(--teal-dark) 100%);
  }

  /* Frames */
  .greeting-frame {
    position: absolute;
    border: 24px solid var(--frame-wood);
    outline: 2px solid var(--frame-edge);
    box-shadow: inset 0 0 0 3px var(--frame-edge), 6px 8px 14px rgba(0,0,0,.35);
    background: linear-gradient(135deg, #f2e7b6, var(--card-paper) 60%, #dccb8e);
  }
  .frame-wishes {
    left: 20px; top: 329px; width: 410px; height: 545px;
    transform: rotate(-4deg);
  }
  .frame-news {
    left: 424px; top: 439px; width: 372px; height: 510px;
    transform: rotate(6deg);
  }
  .script-heading {
    position: absolute;
    font-family: "Courgette", cursive;
    font-weight: 400;
    color: var(--script-red);
    line-height: 33px;
    white-space: nowrap;
  }
  .body-copy {
    position: absolute;
    color: var(--ink);
    white-space: nowrap;
  }
  .frame-wishes .script-heading { left: 47px; top: 62px; font-size: 25px; }
  .frame-wishes .body-copy { left: 56px; top: 191px; font-size: 25px; line-height: 25px; }
  .frame-wishes .body-copy p + p { margin-top: 29px; padding-left: 9px; }

  .frame-news .script-heading { left: 20px; right: 0; top: 46px; text-align: center; font-size: 26px; }
  .frame-news .body-copy { font-size: 24px; line-height: 28px; }
  .news-update { left: 0; right: 38px; top: 136px; text-align: center; }
  .news-invite { left: 32px; top: 254px; }
  .site-link { color: var(--script-red); text-decoration: none; }

  /* Name tag */
  .brand-tag {
    position: absolute;
    left: 323px; top: 842px;
    width: 268px; height: 96px;
    background: var(--tag-paper);
    border-radius: 6px;
    transform: rotate(8deg);
    box-shadow: 3px 5px 10px rgba(0,0,0,.3);
    display: flex; align-items: center; justify-content: center;
    padding-left: 24px;
  }
  .brand-tag::before {
    content: "";
    position: absolute; left: 16px; top: 40px;
    width: 16px; height: 16px; border-radius: 50%;
    background: var(--gold-deep);
  }
  .brand-name {
    font-family: "Roboto", Arial, sans-serif;
    font-weight: 700;
    font-size: 48px;
    color: var(--ink);
  }
</style>
</head>
<body>
<main class="card">
  <div class="pine-zone pine-top-left" role="img" aria-label="Pine branches with golden baubles and sparkles"></div>
  <div class="pine-zone pine-top-right" role="img" aria-label="Pine branches with golden bauble and light garland"></div>
  <div class="pine-zone pine-bottom" role="img" aria-label="Pine branches with glittering golden stars"></div>

  <h1 class="year-title" aria-label="2021">
    <span class="year-digits year-digits-lead" aria-hidden="true">2</span>
    <span class="year-ornament" role="img" aria-label="Green Christmas bauble forming the zero"></span>
    <span class="year-digits year-digits-tail" aria-hidden="true">21</span>
  </h1>

  <section class="greeting-frame frame-wishes">
    <h2 class="script-heading">We wish you a Happy<br>Holiday and a Marvelous<br>New Year 2021!</h2>
    <div class="body-copy">
      <p>As December is the<br>month of giving, we<br>have a surprise for you.</p>
      <p>Please contact your<br>dedicated Account<br>Manager to find<br>out more!</p>
    </div>
  </section>

  <section class="greeting-frame frame-news">
    <h2 class="script-heading">Good news never<br>comes alone !</h2>
    <p class="body-copy news-update">We've also updated<br>our website in order<br>to serve you better.</p>
    <p class="body-copy news-invite">We hope you like it as<br>much as we do.<br>Please enjoy the<br>experience:<br><a class="site-link" href="https://quenlax.example">www.quenlax.example</a></p>
  </section>

  <div class="brand-tag"><span class="brand-name">Quenlax</span></div>
</main>
</body>
</html>
```